Sales PowerPoint Template to help us attract new customers

We need to create a generic PowerPoint template for our organization. We are in the commercial facilities industry, servicing convenience, restaurants, grocery, and retail customers in the US. We handle trades such as HVAC, Refrigeration, Plumbing, Electrical, Food Equipment, Coffee, etc.

We need to incorporate our new logo, updated colors, Font (Arial). We want it to stand out in this deck and avoid looking like all other facility companies. We want to make sure the template size is not too large (less than 20 MB), so it prevent people to edit/send.
Attached are new logo, colors, old powerpoint template, and finally the "New Design to Incorporate into Template" is new materials we're looking to leverage. This might give you ideas.

Create at least 10 slides (1 cover, 1 agenda slide, at least 7 general slides, and 1 wrap-up slide)

Target Market(s)

Convenience Stores, Retail Stores, Groceries, and Restaurants in the US

Industry/Entity Type

Facilities Services (HVAC, Refrigeration, Plumbing, Electrical, etc, repair and preventative maintenance)

Font styles to use
Other font styles liked:
• Arial

Requirements
Must have
• Follow company colors and font (Arial)
Should not have
• Not approved company colors, font

```html
<!DOCTYPE html>
<html lang="en">
<head>
<meta charset="utf-8">
<title>NORVA Facility Solutions – Sales Deck Template</title>
<link rel="stylesheet" href="https://fonts.googleapis.com/css2?family=Montserrat:wght@400;500;600;700;800&display=swap">
<style>
:root{
  --board:#2b2b2b;
  --olive:#8b9a2f;
  --olive-light:#a5ae57;
  --olive-dark:#6f7c22;
  --brown:#8c5a23;
  --amber:#f0a300;
  --ink:#3b3b3b;
  --grey:#9a9a9a;
  --pale:#eeeeee;
  --white:#ffffff;
}
*{box-sizing:border-box;margin:0;padding:0}
html,body{width:844px;height:1200px;overflow:hidden;background:var(--board);font-family:"Montserrat",Arial,sans-serif;color:var(--ink)}
.slide{position:absolute;width:366px;height:206px;overflow:hidden;background:var(--white)}
.col-a{left:57px}.col-b{left:431px}
.row-1{top:63px}.row-2{top:278px}.row-3{top:493px}.row-4{top:709px}.row-5{top:924px}
.abs{position:absolute}
.photo{position:absolute}
.brand{position:absolute;line-height:1}
.brand-name{font-weight:500;letter-spacing:2.4px;color:var(--olive);font-size:12px}
.brand-tag{font-size:5.5px;color:var(--olive);margin-top:2px;padding-left:24px}
.brand.small .brand-name{font-size:5.5px;letter-spacing:1.2px;color:var(--white)}
.brand.small .brand-tag{font-size:2.3px;color:var(--white);padding-left:8px;margin-top:1px}
.brand.small.green .brand-name,.brand.small.green .brand-tag{color:var(--olive)}
.meta{font-size:5px;letter-spacing:1.3px;font-weight:700;color:var(--brown)}
.meta span{color:var(--grey);font-weight:500}
.big-title{font-weight:800;font-size:18.5px;line-height:22px;color:#555}
.big-title em{font-style:normal;color:var(--olive)}
.btn{position:absolute;height:7.5px;border-radius:4px;background:var(--brown);color:var(--white);font-size:4.8px;font-weight:600;text-align:center;line-height:7.5px}
.btn-arrow{position:absolute;width:8px;height:1px;background:var(--grey)}
.btn-arrow::after{content:"";position:absolute;right:0;top:-1.5px;border-left:3px solid var(--grey);border-top:2px solid transparent;border-bottom:2px solid transparent}
.url{position:absolute;left:16px;top:14px;font-size:3.8px;color:var(--ink)}
.rule{position:absolute;top:16px;height:.5px;background:var(--ink)}
.h-slide{font-weight:700;font-size:12.5px;line-height:13.5px}
.kicker{font-size:4.3px;letter-spacing:.9px;font-weight:600}
.lorem{font-size:3.6px;line-height:6.2px}
.vertical{position:absolute;font-size:3px;color:var(--grey);transform:rotate(-90deg);transform-origin:left top;white-space:nowrap}
.pagenum{position:absolute;font-size:3px;color:var(--ink)}
.data-table{position:absolute;border-collapse:collapse;font-size:2.6px;color:var(--ink);table-layout:fixed}
.data-table th{background:var(--olive);color:var(--white);font-weight:500;height:8px}
.data-table td{height:8px;padding:0 2px;text-align:right}
.data-table td:first-child{text-align:left}
.data-table tr:nth-child(even) td{background:#e9e9e9}
.data-table tr:nth-child(odd) td{background:#f6f6f6}
.data-table.short td{height:7.8px}
.search{position:absolute;height:8px;border-radius:4px;background:rgba(255,255,255,.22);font-size:2.8px;color:rgba(255,255,255,.6);padding-left:6px;line-height:8px}
.avatar{position:absolute;width:9px;height:9px;border-radius:50%;background:rgba(255,255,255,.85)}
.tab{position:absolute;top:88px;height:15px;border-radius:6px 6px 0 0;font-size:4.7px;font-weight:700;letter-spacing:.4px;text-align:center;line-height:15px;color:var(--white)}
.field-label{font-size:3.4px;font-weight:600}
.field-value{font-weight:600}
</style>
</head>
<body>

<!-- Cover A -->
<section class="slide col-a row-1">
  <svg class="abs" width="366" height="206" viewBox="0 0 366 206" style="left:0;top:0">
    <polygon points="62,0 238,0 146,94 108,94" fill="#7a6048"/>
    <polygon points="0,56 64,100 140,100 250,206 0,206" fill="#5b5f52"/>
    <polygon points="64,100 140,100 250,206 168,206" fill="#8b9a2f" opacity=".88"/>
  </svg>
  <div class="photo" role="img" aria-label="Smiling couple in a café" style="left:120px;top:0;width:1px;height:1px"></div>
  <div class="photo" role="img" aria-label="Coffee machine behind a counter" style="left:20px;top:140px;width:1px;height:1px"></div>
  <div class="brand" style="left:16px;top:22px"><div class="brand-name">NORVA</div><div class="brand-tag">Facility Solutions</div></div>
  <div class="abs meta" style="left:208px;top:76px">5/15/2025 – <span>Speaker</span></div>
  <div class="abs big-title" style="left:206px;top:86px">PRESENTATION<br><em>TITLE</em></div>
  <div class="abs" style="left:208px;top:128px;font-size:8.3px;font-weight:600;color:#b2b2b2">Enter your subtitle here</div>
  <div class="btn" style="left:260px;top:154px;width:47px">Learn More</div>
  <div class="btn-arrow" style="left:312px;top:158px"></div>
</section>

<!-- Cover B -->
<section class="slide col-b row-1">
  <svg class="abs" width="366" height="206" viewBox="0 0 366 206" style="left:0;top:0" role="img" aria-label="Chefs plating dishes in a restaurant kitchen">
    <polygon points="250,0 366,0 366,206 96,206" fill="#6b5c4e"/>
    <polygon points="40,206 96,206 128,174 96,166" fill="#8b9a2f"/>
  </svg>
  <div class="brand" style="left:16px;top:22px"><div class="brand-name">NORVA</div><div class="brand-tag">Facility Solutions</div></div>
  <div class="abs meta" style="left:27px;top:61px">5/15/2025 – <span>Speaker</span></div>
  <div class="abs big-title" style="left:25px;top:70px">PRESENTATION<br><em>TITLE</em></div>
  <div class="btn" style="left:27px;top:122px;width:46px">Learn More</div>
  <div class="btn-arrow" style="left:78px;top:126px"></div>
</section>

<!-- Section divider -->
<section class="slide col-a row-2" style="background:var(--olive-light)">
  <div class="abs" style="left:19px;top:19px;width:328px;height:168px;border-radius:10px;background:var(--olive);overflow:hidden">
    <div class="photo" role="img" aria-label="Smiling man opening a grocery fridge door" style="left:164px;top:0;width:164px;height:168px;background:linear-gradient(120deg,#4e5a62,#9aa3a6 60%,#d8d8d2)"></div>
  </div>
  <svg class="abs" style="left:96px;top:316px" width="0" height="0"></svg>
  <svg class="abs" style="left:96px;top:47px;left:96px" width="0" height="0"></svg>
  <svg class="abs" style="left:96px;top:46px" width="1" height="1"></svg>
  <svg class="abs" style="left:97px;top:46px;left:96px" width="1" height="1"></svg>
  <svg class="abs" style="left:96px;top:46px" width="1" height="1"></svg>
  <svg class="abs" style="left:96px;top:46px" width="1" height="1"></svg>
  <svg class="abs" style="left:96px;top:46px" width="1" height="1"></svg>
  <svg class="abs" style="left:96px;top:45px" width="1" height="1"></svg>
  <svg class="abs" viewBox="0 0 14 20" width="14" height="19" style="left:96px;top:46px;left:96px"></svg>
  <svg class="abs" viewBox="0 0 14 20" width="14" height="19" style="left:96px;top:45px"></svg>
  <svg class="abs" viewBox="0 0 14 20" width="14" height="19" style="left:96px;top:46px"></svg>
  <svg class="abs" viewBox="0 0 14 20" width="13" height="18" style="left:96px;top:46px"></svg>
  <svg class="abs" viewBox="0 0 14 20" width="13" height="18" style="left:96px;top:46px;left:96px"></svg>
  <svg class="abs" viewBox="0 0 14 20" width="13" height="18" style="left:96px;top:46px;left:96px"></svg>
  <svg class="abs" viewBox="0 0 14 20" width="13" height="18" style="left:96px;top:316px"></svg>
  <svg class="abs" viewBox="0 0 14 20" width="13" height="18" style="left:96px;top:47px;left:96px"></svg>
  <svg class="abs" viewBox="0 0 14 20" width="13" height="18" style="left:96px;top:46px;left:40px"><path d="M4 0v5M10 0v5M1 5h12v5a6 6 0 0 1-12 0zM7 15v5" stroke="#fff" stroke-width="2" fill="#fff"/><path d="M8 6l-3 5h3l-2 4" stroke="#8b9a2f" stroke-width="1.2" fill="none"/></svg>
  <div class="abs" style="left:41px;top:66px;font-size:17px;font-weight:700;color:var(--brown)">01</div>
  <div class="abs" style="left:40px;top:86px;font-size:17px;font-weight:700;color:var(--white)">Grocery</div>
  <div class="abs kicker" style="left:43px;top:110px;color:var(--ink)">ENTER YOURSUBTITLE HERE</div>
  <div class="abs lorem" style="left:43px;top:122px;width:72px;color:#e6ead0">Lorem ipsum dolor sit elit, consect loreretur adipiscing nisi aute. ipsum sit elit. Lorem ipsum dolor sit elit.</div>
  <svg class="abs" viewBox="0 0 28 24" width="27" height="23" style="left:136px;top:150px"><path d="M14 23V3M3 13L14 2l11 11" stroke="#fff" stroke-width="3" fill="none"/></svg>
  <div class="brand small" style="left:18px;top:191px"><div class="brand-name">NORVA</div><div class="brand-tag">Facility Solutions</div></div>
</section>

<!-- Tables and diagrams -->
<section class="slide col-b row-2">
  <div class="url">www.yoursite.com</div>
  <div class="rule" style="left:97px;width:168px"></div>
  <div class="abs h-slide" style="left:34px;top:33px">Tables and<br>Diagrams</div>
  <div class="abs kicker" style="left:34px;top:67px;color:var(--grey)">ENTER YOUR SUBTITLE HERE</div>
  <table class="data-table" style="left:33px;top:83px;width:140px">
    <tr><th style="width:46px">Description 1</th><th colspan="2">Description 2</th><th colspan="2">Description 3</th></tr>
    <tr><td></td><td>Text</td><td>Text</td><td>Text</td><td>Text</td></tr>
    <tr><td>Placeholder text</td><td>xxx</td><td>xxx</td><td>xxx</td><td>xxx</td></tr>
    <tr><td>Placeholder text</td><td>xxx</td><td>xxx</td><td>xxx</td><td>xxx</td></tr>
    <tr><td>Placeholder text</td><td>xxx</td><td>xxx</td><td>xxx</td><td>xxx</td></tr>
    <tr><td>Placeholder text</td><td>xxx</td><td>xxx</td><td>xxx</td><td>xxx</td></tr>
    <tr><td>Placeholder text</td><td>xxx</td><td>xxx</td><td>xxx</td><td>xxx</td></tr>
    <tr><td>Placeholder text</td><td>xxx</td><td>xxx</td><td>xxx</td><td>xxx</td></tr>
    <tr><td>Placeholder text</td><td>xxx</td><td>xxx</td><td>xxx</td><td>xxx</td></tr>
    <tr><td>Placeholder text</td><td>xxx</td><td>xxx</td><td>xxx</td><td>xxx</td></tr>
    <tr><td>Placeholder text</td><td>xxx</td><td>xxx</td><td>xxx</td><td>xxx</td></tr>
  </table>
  <svg class="abs" viewBox="0 0 20 20" width="19" height="19" style="left:186px;top:108px"><path d="M1 10h16M9 2l8 8-8 8" stroke="#8c5a23" stroke-width="2.4" fill="none"/></svg>
  <svg class="abs" viewBox="0 0 120 70" width="120" height="70" style="left:212px;top:83px;font-family:Montserrat,Arial,sans-serif">
    <g font-size="4" fill="#555">
      <text x="0" y="4">160</text><text x="0" y="17">120</text><text x="2" y="29.5">80</text><text x="2" y="42">40</text><text x="5" y="55">0</text>
      <text x="18" y="64">Jan</text><text x="32" y="64">Feb</text><text x="46" y="64">Mar</text><text x="59" y="64">Apr</text><text x="73" y="64">May</text><text x="86" y="64">Jun</text>
    </g>
    <g stroke="#e4e4e4" stroke-width=".4"><line x1="12" y1="2.5" x2="108" y2="2.5"/><line x1="12" y1="15" x2="108" y2="15"/><line x1="12" y1="27.5" x2="108" y2="27.5"/><line x1="12" y1="40" x2="108" y2="40"/><line x1="12" y1="53" x2="108" y2="53"/></g>
    <path d="M12 53L22 38L36 32L50 27L62 20L74 10L93 6V53Z" fill="#f0a300"/>
    <path d="M12 53L22 42L36 38L50 33L62 30L74 26L93 24V53Z" fill="#d6d6d6"/>
  </svg>
  <div class="abs" style="left:315px;top:109px;width:37px;height:37px;border-radius:50%;background:var(--olive);color:#fff;text-align:center">
    <div style="font-size:9px;font-weight:700;margin-top:8px">79%</div>
    <div style="font-size:3.2px;line-height:5px;margin-top:1px">Lorem ipsum<br>dolor sit</div>
  </div>
  <div class="abs lorem" style="left:220px;top:152px;width:110px;text-align:center;color:#777">Lorem ipsum dolor sit elit, consect loreretur adipiscing nisi aute. ipsum sit elit. Lorem ipsum dolor</div>
  <div class="brand small green" style="left:21px;top:187px"><div class="brand-name">NORVA</div><div class="brand-tag">Facility Solutions</div></div>
  <div class="vertical" style="left:354px;top:192px">Presentation Title</div>
  <div class="pagenum" style="left:355px;top:198px">4</div>
</section>

<!-- Cycle diagram -->
<section class="slide col-a row-3">
  <div class="abs" style="left:0;top:0;width:122px;height:206px;background:var(--olive)"></div>
  <div class="abs" style="left:122px;top:0;width:122px;height:206px;background:linear-gradient(90deg,#ffffff,#e9e9e9)"></div>
  <div class="url">www.yoursite.com</div>
  <div class="rule" style="left:66px;width:198px"></div>
  <svg class="abs" viewBox="0 0 20 20" width="19" height="19" style="left:27px;top:45px"><path d="M10 1v16M2 9l8 8 8-8" stroke="#fff" stroke-width="2.2" fill="none"/></svg>
  <div class="abs h-slide" style="left:27px;top:76px;color:var(--white)">Tables and<br>Diagrams</div>
  <div class="abs kicker" style="left:27px;top:110px;color:var(--white)">ENTER YOUR SUBTITLE HERE</div>
  <div class="abs lorem" style="left:27px;top:128px;width:60px;color:#eef0dc">Lorem ipsum dolor sit elit. consect loreretur adipiscing nisi aute. ipsum sit elit. Lorem ipsum dolor sit elit.</div>
  <div class="brand small" style="left:21px;top:189px"><div class="brand-name">NORVA</div><div class="brand-tag">Facility Solutions</div></div>

  <svg class="abs" viewBox="-50 -50 100 100" width="100" height="100" style="left:194px;top:53px">
    <g fill="none" stroke-width="17">
      <path d="M-38 0A38 38 0 0 1 0 -38" stroke="#8b9a2f"/>
      <path d="M0 -38A38 38 0 0 1 38 0" stroke="#8c5a23"/>
      <path d="M38 0A38 38 0 0 1 0 38" stroke="#f0a300"/>
      <path d="M0 38A38 38 0 0 1 -38 0" stroke="#3b3b3b"/>
    </g>
    <polygon points="0,-50 12,-38 0,-26" fill="#8b9a2f"/>
    <polygon points="50,0 38,12 26,0" fill="#8c5a23"/>
    <polygon points="0,50 -12,38 0,26" fill="#f0a300"/>
    <polygon points="-50,0 -38,-12 -26,0" fill="#3b3b3b"/>
    <circle r="28" fill="#fff"/>
  </svg>
  <svg class="abs" viewBox="0 0 20 14" width="18" height="13" style="left:235px;top:83px"><circle cx="7" cy="4" r="3.2" fill="#3b3b3b"/><path d="M1 14a6 6 0 0 1 12 0z" fill="#3b3b3b"/><circle cx="13" cy="3" r="2.8" fill="#3b3b3b"/><path d="M12 7a5.5 5.5 0 0 1 7 7h-5" fill="#3b3b3b"/></svg>
  <div class="abs" style="left:224px;top:96px;width:40px;text-align:center;font-size:9px;font-weight:700">832.524</div>
  <div class="abs lorem" style="left:224px;top:107px;width:40px;text-align:center;font-size:3.2px;line-height:5.6px">Lorem ipsum dolor sit elit. consect lorer</div>

  <div class="abs" style="left:155px;top:38px;width:55px"><div class="kicker" style="font-weight:700">INSERT TITLE</div><div class="lorem" style="margin-top:3px;color:#777">Lorem ipsum dolor sit elit. consect loreretur Lorem ipsum dolor sit Lorem ipsum dolor elit, consect Lorem ipsum dolor sit elit, consect loreretur</div></div>
  <div class="abs" style="left:287px;top:38px;width:55px"><div class="kicker" style="font-weight:700">INSERT TITLE</div><div class="lorem" style="margin-top:3px;color:#777">Lorem ipsum dolor sit elit. consect loreretur Lorem ipsum dolor sit Lorem ipsum dolor sit elit. consect</div></div>
  <div class="abs" style="left:155px;top:124px;width:55px"><div class="kicker" style="font-weight:700">INSERT TITLE</div><div class="lorem" style="margin-top:3px;color:#777">Lorem ipsum dolor sit elit. consect loreretur Lorem ipsum dolor sit Lorem ipsum dolor sit elit. consect Lorem ipsum dolor sit elit. consect loreretur Lorem ipsum dolor sit Lorem</div></div>
  <div class="abs" style="left:287px;top:136px;width:55px"><div class="kicker" style="font-weight:700">INSERT TITLE</div><div class="lorem" style="margin-top:3px;color:#777">Lorem ipsum dolor sit elit. consect loreretur Lorem ipsum dolor sit Lorem ipsum dolor sit elit. consect</div></div>
  <div class="vertical" style="left:354px;top:192px">Presentation Title</div>
  <div class="pagenum" style="left:355px;top:198px">5</div>
</section>

<!-- Icon features over photo -->
<section class="slide col-b row-3" style="background:var(--olive)">
  <div class="photo" role="img" aria-label="Woman pushing a cart down a grocery aisle, tinted green" style="left:0;top:0;width:366px;height:206px;background:linear-gradient(90deg,#6d7a2a,#8b9a2f 40%,#a1a258 60%,#7c8a2c)"></div>
  <div class="search" style="left:280px;top:11px;width:60px">Search here</div>
  <div class="avatar" style="left:346px;top:11px"></div>
  <svg class="abs" viewBox="0 0 20 20" width="19" height="19" style="left:43px;top:25px"><path d="M10 1v16M2 9l8 8 8-8" stroke="#fff" stroke-width="2.2" fill="none"/></svg>
  <div class="abs h-slide" style="left:44px;top:57px;color:var(--white)">Tables and<br>Diagrams</div>
  <svg class="abs" viewBox="0 0 14 20" width="17" height="23" style="left:60px;top:99px"><path d="M4 0v5M10 0v5M1 5h12v5a6 6 0 0 1-12 0zM7 15v5" stroke="#fff" stroke-width="2" fill="#fff"/><path d="M8 6l-3 5h3l-2 4" stroke="#8b9a2f" stroke-width="1.2" fill="none"/></svg>
  <svg class="abs" viewBox="0 0 44 28" width="44" height="28" style="left:156px;top:95px"><rect x="9" y="2" width="26" height="24" stroke="#fff" stroke-width="1.6" fill="none"/><line x1="22" y1="2" x2="22" y2="26" stroke="#fff" stroke-width="1.4"/><path d="M1 14h12M4 11l-3 3 3 3M31 14h12M40 11l3 3-3 3" stroke="#fff" stroke-width="1.6" fill="none"/></svg>
  <svg class="abs" viewBox="0 0 26 34" width="24" height="32" style="left:272px;top:92px"><path d="M7 1v7M4 5l3 3 3-3M18 8V1M15 4l3-3 3 3" stroke="#fff" stroke-width="1.6" fill="none"/><rect x="1" y="11" width="24" height="22" stroke="#fff" stroke-width="1.6" fill="none"/><circle cx="8" cy="16" r="2" fill="#fff"/><circle cx="18" cy="16" r="2" fill="#fff"/><rect x="5.5" y="19" width="5" height="10" fill="#fff"/><rect x="15.5" y="19" width="5" height="10" fill="#fff"/></svg>
  <div class="abs" style="left:33px;top:128px;width:70px;text-align:center;font-size:5.3px;line-height:7.6px;color:rgba(255,255,255,.8)">THIS IS A<br>PLACEHOLDER<br>TEXT.<br>THIS TEXT CAN<br>BE REPLACED<br>WITH<br>YOUR OWN TEXT.</div>
  <div class="abs" style="left:143px;top:128px;width:70px;text-align:center;font-size:5.3px;line-height:7.6px;color:rgba(255,255,255,.8)">THIS IS A<br>PLACEHOLDER<br>TEXT.<br>THIS TEXT CAN<br>BE REPLACED<br>WITH<br>YOUR OWN TEXT.</div>
  <div class="abs" style="left:250px;top:128px;width:70px;text-align:center;font-size:5.3px;line-height:7.6px;color:rgba(255,255,255,.8)">THIS IS A<br>PLACEHOLDER<br>TEXT.<br>THIS TEXT CAN<br>BE REPLACED<br>WITH<br>YOUR OWN TEXT.</div>
  <div class="brand small" style="left:21px;top:189px"><div class="brand-name">NORVA</div><div class="brand-tag">Facility Solutions</div></div>
  <div class="pagenum" style="left:355px;top:198px;color:#fff">6</div>
</section>

<!-- Tabs and contact -->
<section class="slide col-a row-4">
  <div class="photo" role="img" aria-label="Cashier serving customers at a supermarket checkout" style="left:0;top:0;width:366px;height:103px;background:linear-gradient(90deg,#3f4a55,#7b7068 45%,#b7a592 70%,#6e5d52)"></div>
  <div class="tab" style="left:19px;width:83px;background:var(--white);color:var(--ink)">FIRST DESCRIPTION</div>
  <div class="tab" style="left:102px;width:80px;background:var(--olive)">SECOND DESCRIPTION</div>
  <div class="tab" style="left:183px;width:82px;background:var(--brown)">THIRD DESCRIPTION</div>
  <div class="tab" style="left:265px;width:81px;background:var(--olive)">FOURTH DESCRIPTION</div>
  <div class="abs" style="left:29px;top:119px;font-size:12px;font-weight:600;line-height:13.5px;color:#444">enter Your two<br>line title here</div>
  <div class="abs lorem" style="left:29px;top:154px;width:72px;color:#777">Lorem ipsum dolor sit elit, consect loreretur adipiscing nisi aute. ipsum sit elit. Lorem ipsum dolor sit</div>
  <div class="abs lorem" style="left:29px;top:177px;width:72px;color:#777">Lorem ipsum dolor sit elit, consect loreretur adipiscing nisi a</div>
  <div class="abs" style="left:148px;top:124px">
    <div class="field-label">Calendar</div><div class="field-value" style="font-size:9px">January 28</div>
    <div class="field-label" style="margin-top:5px">Phone</div><div class="field-value" style="font-size:9px">+1234567890</div>
    <div class="field-label" style="margin-top:5px">Address</div><div class="field-value" style="font-size:5.6px;line-height:6.4px">Small Town st. 89<br>TX, United States</div>
  </div>
  <table class="data-table short" style="left:233px;top:135px;width:108px">
    <tr><th>Description 1</th><th>Description 2</th><th>Description 3</th></tr>
    <tr><td>Placeholder text</td><td>xxx</td><td>xxx</td></tr>
    <tr><td>Placeholder text</td><td>xxx</td><td>xxx</td></tr>
    <tr><td>Placeholder text</td><td>xxx</td><td>xxx</td></tr>
    <tr><td>Placeholder text</td><td>xxx</td><td>xxx</td></tr>
  </table>
</section>

<!-- Phone mockup -->
<section class="slide col-b row-4" style="background:var(--olive)">
  <div class="url" style="color:#fff">www.yoursite.com</div>
  <div class="rule" style="left:97px;width:168px;background:#3b3b3b"></div>
  <div class="photo" role="img" aria-label="Hand holding a smartphone, black and white" style="left:60px;top:110px;width:140px;height:96px;border-radius:60px 60px 0 0;background:linear-gradient(180deg,#bdbdbd,#7a7a7a)"></div>
  <div class="abs" style="left:115px;top:24px;width:72px;height:148px;border-radius:10px;background:#1e1e1e;padding:3px">
    <div role="img" aria-label="Smiling café staff on the phone screen" style="position:relative;width:100%;height:100%;border-radius:8px;background:linear-gradient(180deg,#7a6656,#c9a88a 55%,#5f6a78)">
      <div class="brand small" style="left:16px;top:21px"><div class="brand-name">NORVA</div><div class="brand-tag">Facility Solutions</div></div>
    </div>
  </div>
  <svg class="abs" viewBox="0 0 20 18" width="18" height="16" style="left:206px;top:51px"><path d="M2 2l7 7-7 7M10 2l7 7-7 7" stroke="#8c5a23" stroke-width="2.6" fill="none"/></svg>
  <div class="abs" style="left:234px;top:45px;font-size:16px;font-weight:700;line-height:18.5px;color:#fff">Hands-on<br>phone<br>mockups</div>
  <div class="abs lorem" style="left:234px;top:113px;width:100px;color:#eef0dc">Lorem ipsum dolor sit elit, consect loreretur adipiscing nisi aute. ipsum sit elit. Lorem ipsum dolor sit elit. Lorem ipsum dolor sit elit, consect loreretur adipiscing nisi aute. ipsum sit elit. Lorem ipsum dolor sit elit. Lorem ipsum dolor sit elit, consect loreretur adipiscing nisi aute. ipsum sit elit. Lorem ipsum dolor sit elit. Lorem ipsum dolor sit elit, consect loreretur adipiscing nisi aute. ipsum sit elit. Lorem ipsum dolor sit elit.</div>
  <div class="brand small" style="left:21px;top:189px"><div class="brand-name">NORVA</div><div class="brand-tag">Facility Solutions</div></div>
  <div class="vertical" style="left:354px;top:192px;color:#d4d8b0">Presentation Title</div>
  <div class="pagenum" style="left:355px;top:198px">8</div>
</section>

<!-- Desktop mockup -->
<section class="slide col-a row-5">
  <div class="abs" style="left:0;top:175px;width:366px;height:31px;background:linear-gradient(180deg,#fff,#bdbdbd)"></div>
  <div class="url">www.yoursite.com</div>
  <div class="rule" style="left:66px;width:198px"></div>
  <svg class="abs" viewBox="0 0 20 20" width="19" height="19" style="left:31px;top:38px"><path d="M10 1v16M2 9l8 8 8-8" stroke="#8c5a23" stroke-width="2.4" fill="none"/></svg>
  <div class="abs" style="left:31px;top:61px;font-size:16px;font-weight:700;line-height:18.5px;color:#3b3b3b">Simple<br>desktop<br>mockups</div>
  <div class="abs lorem" style="left:32px;top:126px;width:70px;color:#777">Lorem ipsum dolor sit elit, consect loreretur adipiscing nisi aute. ipsum sit elit. Lorem sit elit. Lorem ipsum dolor sit elit. consect loreretur</div>
  <div class="abs" style="left:141px;top:27px;width:200px;height:108px;border-radius:5px 5px 0 0;background:#1c1c1c;padding:8px 8px 0">
    <div role="img" aria-label="Cashier scanning groceries at a checkout" style="position:relative;width:100%;height:100%;background:linear-gradient(120deg,#3c4550,#8a7b6d 50%,#c9b6a0)">
      <div class="brand small" style="left:18px;top:64px"><div class="brand-name">NORVA</div><div class="brand-tag">Facility Solutions</div></div>
    </div>
  </div>
  <div class="abs" style="left:141px;top:135px;width:200px;height:15px;border-radius:0 0 5px 5px;background:linear-gradient(180deg,#e2e2e2,#c8c8c8)"></div>
  <div class="abs" style="left:226px;top:150px;width:30px;height:22px;background:linear-gradient(90deg,#b5b5b5,#e6e6e6,#b5b5b5)"></div>
  <div class="abs" style="left:212px;top:171px;width:58px;height:3px;border-radius:2px;background:#d0d0d0"></div>
  <div class="brand small green" style="left:21px;top:189px"><div class="brand-name" style="color:var(--ink)">NORVA</div><div class="brand-tag" style="color:var(--ink)">Facility Solutions</div></div>
  <div class="vertical" style="left:354px;top:192px">Presentation Title</div>
  <div class="pagenum" style="left:355px;top:198px">9</div>
</section>

<!-- Thank you -->
<section class="slide col-b row-5" style="background:var(--olive)">
  <div class="brand" style="left:20px;top:18px"><div class="brand-name" style="color:#fff;font-size:8px;letter-spacing:1.8px">NORVA</div><div class="brand-tag" style="color:#fff;font-size:3.3px;padding-left:14px">Facility Solutions</div></div>
  <div class="search" style="left:280px;top:11px;width:60px">Search here</div>
  <div class="avatar" style="left:346px;top:11px"></div>
  <div class="abs" style="left:37px;top:58px;font-size:63px;font-weight:700;line-height:1;letter-spacing:-1px;color:#fff">Thank</div>
  <div class="abs" style="left:190px;top:111px;font-size:63px;font-weight:700;line-height:1;letter-spacing:-1px;color:#fff">You</div>
  <div class="abs" style="left:259px;top:82px;font-size:5.2px;line-height:9.5px;color:#e3e7c4">For Joining This<br>Presentation</div>
  <div class="abs" style="left:21px;top:170px;font-size:4.5px;line-height:8.5px;color:#e3e7c4">Every big idea starts small, with a vision to<br>grow beyond the ordinary</div>
</section>

</body>
</html>
```